Fitness center graphic design

Looking for graphics to complete interior of a gym
img 3133 - main entrance, looking for something motivational, eye catching. can include logo but prefer not to
img 9617 looking for something to encourage heavy lifting. something motivating
img 9616 is across from 9617 location. maybe something with logo
img 9614 seen upon entering want something that highlights all our offerings. put a photo for inspriation only
img b37 is streching zone. want it to be labled
img b76 personal training/ group training room. want it to be labled

Target Market(s)

Want graphics to be eye catching. And appeal to all fitness levels

Industry/Entity Type

Fitness gym

Requirements
Must have
• eye catching, bright, motivating qualities
Should not have
• logo in every design

```html
<!DOCTYPE html>
<html lang="en">
<head>
<meta charset="utf-8">
<title>Gym Interior Graphics</title>
<link rel="stylesheet" href="https://fonts.googleapis.com/css2?family=Oswald:wght@500;700&display=swap">
<style>
  :root {
    --orange: #f15a24;
    --orange-deep: #d9481a;
    --black: #121212;
    --cream: #f6dcb8;
    --khaki: #8c7b63;
    --white: #ffffff;
    --canvas: #ececec;
  }
  * { margin: 0; padding: 0; box-sizing: border-box; }
  html, body { width: 1200px; height: 660px; overflow: hidden; background: var(--canvas); }
  body { font-family: "Oswald", sans-serif; }
  .board {
    width: 1200px; height: 660px; padding: 20px;
    display: grid;
    grid-template-columns: repeat(3, 1fr);
    grid-template-rows: repeat(2, 1fr);
    gap: 20px;
  }
  .cell { display: flex; align-items: center; justify-content: center; }
  .graphic { display: block; }
  .graphic text { font-family: "Oswald", sans-serif; font-weight: 700; }
</style>
</head>
<body>
<main class="board">

  <!-- Main entrance banner -->
  <section class="cell entrance-banner">
    <svg class="graphic" width="373" height="120" viewBox="0 0 373 120">
      <rect width="373" height="120" fill="var(--black)"/>
      <polygon points="0,0 110,0 70,120 0,120" fill="var(--orange)"/>
      <rect x="12" y="12" width="78" height="96" fill="var(--orange-deep)" role="img" aria-label="Illustration of a person bench pressing a barbell"/>
      <polygon points="250,8 300,8 290,20 240,20" fill="var(--orange)"/>
      <polygon points="300,100 350,100 340,112 290,112" fill="var(--orange)"/>
      <text x="106" y="67" font-size="16" fill="var(--white)" textLength="254" lengthAdjust="spacingAndGlyphs">THE BODY ACHIEVES WHAT THE MIND BELIEVES</text>
    </svg>
  </section>

  <!-- Training zone doorway -->
  <section class="cell training-zone">
    <svg class="graphic" width="300" height="300" viewBox="0 0 300 300">
      <rect width="300" height="300" fill="var(--orange)"/>
      <polygon points="300,60 300,300 230,300 300,150" fill="var(--black)"/>
      <polygon points="190,90 300,20 300,60 240,90" fill="var(--black)"/>
      <rect x="36" y="95" width="228" height="205" fill="var(--canvas)"/>
      <text x="150" y="62" font-size="34" fill="var(--cream)" text-anchor="middle" letter-spacing="1">TRAINING ZONE</text>
    </svg>
  </section>

  <!-- Personal and group training mural -->
  <section class="cell training-mural">
    <svg class="graphic" width="373" height="170" viewBox="0 0 373 170">
      <rect width="373" height="170" fill="var(--black)"/>
      <polygon points="150,170 373,0 373,70 240,170" fill="var(--orange)"/>
      <polygon points="110,170 160,130 175,130 125,170" fill="var(--orange)"/>
      <rect x="285" y="18" width="72" height="140" fill="var(--orange-deep)" role="img" aria-label="Illustration of a person lifting two dumbbells overhead"/>
      <text x="16" y="36" font-size="13" fill="var(--orange)" textLength="230" lengthAdjust="spacingAndGlyphs">YOUR BODY CAN STAND ALMOST ANYTHING.</text>
      <text x="16" y="54" font-size="13" fill="var(--orange)" textLength="245" lengthAdjust="spacingAndGlyphs">IT'S YOUR MIND THAT YOU HAVE TO CONVINCE.</text>
    </svg>
  </section>

  <!-- Heavy lifting banner -->
  <section class="cell lifting-banner">
    <svg class="graphic" width="373" height="110" viewBox="0 0 373 110">
      <rect width="373" height="110" fill="var(--orange)"/>
      <polygon points="0,0 110,0 80,110 0,110" fill="var(--black)"/>
      <polygon points="330,60 373,30 373,110 320,110" fill="var(--black)"/>
      <rect x="12" y="10" width="68" height="90" fill="var(--orange-deep)" role="img" aria-label="Illustration of a woman lifting a barbell"/>
      <text x="104" y="48" font-size="13" fill="var(--white)" textLength="214" lengthAdjust="spacingAndGlyphs">IF YOU THINK LIFTING WEIGHTS IS DANGEROUS,</text>
      <text x="104" y="68" font-size="13" fill="var(--white)" textLength="206" lengthAdjust="spacingAndGlyphs">TRY BEING WEAK. BEING WEAK IS DANGEROUS.</text>
    </svg>
  </section>

  <!-- Club name wall -->
  <section class="cell club-wall">
    <svg class="graphic" width="373" height="150" viewBox="0 0 373 150">
      <rect width="373" height="150" fill="var(--black)"/>
      <polygon points="0,40 60,0 120,0 0,90" fill="var(--orange)"/>
      <rect x="20" y="18" width="100" height="114" fill="var(--orange-deep)" role="img" aria-label="Illustration of a person doing a bench exercise"/>
      <rect x="135" y="0" width="238" height="150" fill="var(--black)"/>
      <polygon points="300,150 373,60 373,150" fill="var(--orange)"/>
      <polygon points="330,0 373,0 373,30" fill="var(--orange)"/>
      <circle cx="155" cy="78" r="11" fill="var(--white)"/>
      <text x="173" y="85" font-size="19" fill="var(--white)" textLength="178" lengthAdjust="spacingAndGlyphs">SUMMIT STRENGTH CLUB</text>
    </svg>
  </section>

  <!-- Stretching zone column -->
  <section class="cell stretching-zone">
    <svg class="graphic" width="150" height="300" viewBox="0 0 150 300">
      <rect width="150" height="300" fill="var(--orange)"/>
      <polygon points="0,190 150,110 150,300 0,300" fill="var(--khaki)"/>
      <polygon points="0,265 150,195 150,220 0,290" fill="var(--orange)"/>
      <text x="0" y="0" font-size="26" fill="var(--white)" transform="translate(20 150) rotate(-45)">STRECHING</text>
      <text x="0" y="0" font-size="26" fill="var(--white)" transform="translate(50 170) rotate(-45)">ZONE</text>
    </svg>
  </section>

</main>
</body>
</html>
```